Training Materials Cover design

Graphic design for the front and back cover of a training manual. Review my website at www.vbtrelmo.com. The business name is Meridale Institute of Trade Vexmo

Target Market(s)

Professional people and those interested in professional and personal development

Requirements
Must have
• Front and back cover. Should include my current logo. The front page title should be 'Trade Adept of Vexmo'

```html
<!DOCTYPE html>
<html lang="en">
<head>
<meta charset="utf-8">
<title>Trade Adept of Vexmo – Manual Cover</title>
<link href="https://fonts.googleapis.com/css2?family=Montserrat:wght@400;500;600;700;800&display=swap" rel="stylesheet">
<style>
  :root {
    --backdrop: #9a9a9a;
    --paper: #eaecea;
    --navy: #172851;
    --green: #137b2b;
    --green-bright: #1c9a35;
    --green-dark: #05170d;
    --white: #ffffff;
    --ink: #1b2a4e;
  }
  * { margin: 0; padding: 0; box-sizing: border-box; }
  html, body { width: 1200px; height: 993px; overflow: hidden; }
  body { background: var(--backdrop); font-family: "Montserrat", Arial, sans-serif; position: relative; }

  .cover {
    position: absolute; left: 86px; top: 120px; width: 1027px; height: 726px;
    background: var(--paper); overflow: hidden;
    box-shadow: 2px 4px 10px rgba(0,0,0,.25);
  }
  .frame-lines { position: absolute; inset: 0; }

  .navy-band { position: absolute; left: 0; top: 130px; width: 100%; height: 216px; background: var(--navy); }
  .accent-square { position: absolute; left: 591px; top: 0; width: 129px; height: 130px; background: var(--green); }
  .accent-shadow { position: absolute; left: 591px; top: 130px; width: 129px; height: 30px; background: var(--green-dark); }

  .brand { position: absolute; display: flex; align-items: center; gap: 6px; }
  .brand-dot { border-radius: 50%; background: var(--green); flex: none; }
  .brand-name { color: var(--green); font-weight: 700; line-height: 1.2; }
  .brand--back { left: 84px; top: 58px; background: var(--paper); padding: 0 4px; }
  .brand--back .brand-dot { width: 34px; height: 34px; }
  .brand--back .brand-name { font-size: 8px; width: 92px; }
  .brand--front { left: 862px; top: 620px; }
  .brand--front .brand-dot { width: 44px; height: 44px; }
  .brand--front .brand-name { font-size: 10px; width: 112px; }

  .section-title { color: var(--white); font-size: 12.5px; font-weight: 700; position: absolute; left: 70px; }
  .section-title::after { content: ""; display: block; width: 28px; height: 1.5px; background: var(--green-bright); margin-top: 5px; }
  .about-title { top: 178px; }
  .about-lead { position: absolute; left: 70px; top: 213px; color: var(--green-bright); font-size: 10px; font-weight: 700; }
  .about-text { position: absolute; left: 70px; top: 226px; width: 400px; color: var(--white); font-size: 10px; line-height: 12.6px; }
  .about-text p + p { margin-top: 4.5px; }

  .cover-title { position: absolute; left: 625px; top: 183px; color: var(--white); font-size: 38px; font-weight: 800; line-height: 35px; letter-spacing: .5px; text-transform: uppercase; }
  .cover-tagline { position: absolute; left: 625px; top: 298px; color: var(--green-bright); font-size: 13.4px; font-weight: 600; line-height: 15.5px; text-transform: uppercase; letter-spacing: .2px; }

  .hero-photo { position: absolute; left: 592px; top: 346px; width: 435px; height: 223px;
    background: linear-gradient(120deg, #b9c6d3 0%, #e6ebef 40%, #2a3650 75%, #1d2841 100%); }
  .hero-bar { position: absolute; left: 592px; top: 569px; width: 435px; height: 6px; background: var(--navy); }
  .hero-bar::before { content: ""; position: absolute; left: 0; top: 0; width: 125px; height: 100%; background: var(--green); }

  .thumbs { position: absolute; left: 73px; top: 381px; display: flex; gap: 7px; }
  .thumb { width: 130px; height: 78px; border: 1px solid var(--green); padding: 4px; background: var(--white); }
  .thumb-fill { width: 100%; height: 100%; }
  .thumb--growth .thumb-fill { background: linear-gradient(135deg, #8fc865, #6fb24a); }
  .thumb--city .thumb-fill { background: linear-gradient(180deg, #e8eef7, #4a5f8c); }
  .thumb--meeting .thumb-fill { background: linear-gradient(90deg, #f1f3f4 40%, #23283a); }

  .contact-title { color: var(--ink); top: 557px; }
  .contact-list { position: absolute; left: 70px; top: 585px; list-style: none; }
  .contact-list li { display: flex; align-items: center; gap: 6px; height: 18px; color: var(--ink); font-size: 8.6px; font-weight: 500; }
  .contact-icon { width: 13px; height: 13px; flex: none; }

  .site-link { position: absolute; color: var(--ink); font-weight: 700; font-size: 14.5px; }
  .site-link--back { left: 76px; top: 651px; background: var(--paper); padding: 0 6px; }
  .site-link--front { left: 625px; top: 651px; border: 1px solid var(--green); padding: 1px 6px; background: var(--paper); line-height: 17px; }
</style>
</head>
<body>
  <div class="cover">
    <div class="navy-band"></div>
    <div class="accent-square"></div>
    <div class="accent-shadow"></div>

    <svg class="frame-lines" width="1027" height="726" viewBox="0 0 1027 726" aria-hidden="true">
      <polyline points="591,77 43,77 43,661 625,661" fill="none" stroke="#1c9a35" stroke-width="0.8"/>
    </svg>

    <div class="brand brand--back">
      <span class="brand-dot"></span>
      <span class="brand-name">Meridale Institute of Trade Vexmo</span>
    </div>

    <h2 class="section-title about-title">About us</h2>
    <p class="about-lead">There is absolutely NO Magic to Vexmo!</p>
    <div class="about-text">
      <p>If we had fifty cents for everytime, we read on a Vexmo related website how it is magically or it will make you magically or the people you apply it to will experience magic we could retire now!</p>
      <p>Look we get the importance of marketing spin in business,but let’s get real. There are some myths regularly observedin the world of Vexmo Training you should brace for yourself for.</p>
    </div>

    <h1 class="cover-title">Trade<br>Adept<br>of Vexmo</h1>
    <p class="cover-tagline">Get the business edge in<br>communication, influence, and mindset</p>

    <div class="hero-photo" role="img" aria-label="Photo of four business colleagues smiling in a meeting around a table"></div>
    <div class="hero-bar"></div>

    <div class="thumbs">
      <div class="thumb thumb--growth"><div class="thumb-fill" role="img" aria-label="Photo of a woman with a laptop in front of a green wall about investing in yourself"></div></div>
      <div class="thumb thumb--city"><div class="thumb-fill" role="img" aria-label="Photo of business people walking through a city, double exposure"></div></div>
      <div class="thumb thumb--meeting"><div class="thumb-fill" role="img" aria-label="Photo of two colleagues reviewing documents at a desk"></div></div>
    </div>

    <h2 class="section-title contact-title">Contact us</h2>
    <ul class="contact-list">
      <li>
        <svg class="contact-icon" viewBox="0 0 14 14" aria-hidden="true"><circle cx="7" cy="7" r="7" fill="#1c9a35"/><path d="M7 3.3a2.3 2.3 0 0 0-2.3 2.3c0 1.8 2.3 4.4 2.3 4.4s2.3-2.6 2.3-4.4A2.3 2.3 0 0 0 7 3.3z" fill="none" stroke="#fff" stroke-width=".9"/><circle cx="7" cy="5.6" r=".8" fill="#fff"/></svg>
        X-2X Lorem Ipsum, City, XX
      </li>
      <li>
        <svg class="contact-icon" viewBox="0 0 14 14" aria-hidden="true"><circle cx="7" cy="7" r="7" fill="#1c9a35"/><path d="M4.5 3.8l1.4-.3.8 1.8-.9.7a4.6 4.6 0 0 0 2.2 2.2l.7-.9 1.8.8-.3 1.4c-3.2.3-6-2.5-5.7-5.7z" fill="none" stroke="#fff" stroke-width=".8" stroke-linejoin="round"/></svg>
        618-XXX-XXX
      </li>
      <li>
        <svg class="contact-icon" viewBox="0 0 14 14" aria-hidden="true"><circle cx="7" cy="7" r="7" fill="#1c9a35"/><rect x="3.6" y="4.6" width="6.8" height="4.8" fill="none" stroke="#fff" stroke-width=".8"/><path d="M3.6 4.6L7 7.4l3.4-2.8" fill="none" stroke="#fff" stroke-width=".8"/></svg>
        xxx@vbtrelmo.com
      </li>
    </ul>

    <span class="site-link site-link--back">www.vbtrelmo.com</span>
    <span class="site-link site-link--front">www.vbtrelmo.com</span>

    <div class="brand brand--front">
      <span class="brand-dot"></span>
      <span class="brand-name">Meridale Institute of Trade Vexmo</span>
    </div>
  </div>
</body>
</html>
```